A multi-page brochure that explains our firm ,KVO Wealth Management

We have a current brochure attached but it is a compilation of several items combined into one. We would like this to have the same content but be one complete theme. We are a financial planning form so it needs to have a level of professionalism but also a comfortable approach for clients and showing that was have a lot of resources and experience. We cater mostly to the 55-60+ age community.

We need the front page picture changed. lake themed would be great, like our website www.TheBaskinCollective.com
Just to be clear we use KVO Wealth Management now as our company name. Parent company name is The Baskin Collective LLC. I attached the current mock brochure and our new logos.
Our logo colors are:
KVO WM Logo Colors:

Blue:
HEX: #0f75bc
RGB: rgba(15,117,188,255)

Grey:
HEX: #6d6e71
RGB: rgba(109,110,113,255)

Target Market(s)

High-level individuals that are looking for financial guidance who are 40 years old and up

Industry/Entity Type

Wealth Management

Requirements
Must have
• Clean and crisp
Nice to have
• https://www.quillmoorplanning.example/wealth-management-brochure , this is a sample we like

```html
<!DOCTYPE html>
<html lang="en">
<head>
<meta charset="utf-8">
<title>KVO Wealth Management Brochure</title>
<link rel="stylesheet" href="https://fonts.googleapis.com/css2?family=Playfair+Display:wght@400;700;900&display=swap">
<style>
  :root {
    --brand-blue: #0f75bc;
    --brand-grey: #6d6e71;
    --backdrop: #e6e6e6;
    --paper: #ffffff;
    --ink: #2b2b2b;
    --body-ink: #555555;
  }
  * { margin: 0; padding: 0; box-sizing: border-box; }
  html, body { width: 1200px; height: 525px; overflow: hidden; }
  body {
    background: var(--backdrop);
    font-family: "Playfair Display", Georgia, serif;
    position: relative;
  }
  .page {
    position: absolute;
    top: 43px;
    width: 339px;
    height: 439px;
    background: var(--paper);
    overflow: hidden;
  }
  .page--cover { left: 48px; }
  .page--partner { left: 431px; }
  .page--philosophy { left: 813px; }

  /* Cover */
  .cover-photo {
    position: absolute;
    left: 8px; top: 9px;
    width: 323px; height: 278px;
    border-top-left-radius: 50px;
    background: linear-gradient(180deg, #bfe0f5 0%, #d8eef8 38%, #7fa9b0 52%, #3c9a9a 68%, #2f6e64 85%, #6b6350 100%);
  }
  .cover-panel {
    position: absolute;
    left: 9px; top: 295px;
    width: 322px; height: 134px;
    background: var(--brand-blue);
    border-bottom-right-radius: 50px;
  }
  .cover-logo-tab {
    position: absolute;
    left: 155px; top: 248px;
    width: 176px; height: 60px;
    background: var(--paper);
    border-radius: 30px 0 0 30px;
    display: flex; align-items: center; justify-content: center;
  }
  .cover-logo-name {
    font-family: "Playfair Display", Georgia, serif;
    font-weight: 400;
    font-size: 14px;
    color: var(--brand-blue);
    line-height: 1.1;
    text-align: center;
  }
  .cover-title {
    position: absolute;
    left: 21px; top: 337px;
    color: var(--paper);
    line-height: 1.18;
  }
  .cover-title strong { display: block; font-weight: 700; font-size: 20.5px; }
  .cover-title span { display: block; font-weight: 400; font-size: 20px; }
  .cover-rule {
    position: absolute;
    left: 23px; top: 395px;
    width: 210px; height: 1px;
    background: rgba(255,255,255,0.8);
  }
  .cover-rule::before {
    content: ""; position: absolute; left: 0; top: -1px;
    width: 72px; height: 3px; background: var(--paper); border-radius: 2px;
  }

  /* Inner pages */
  .page-heading {
    position: absolute;
    left: 16px; top: 38px;
    font-size: 17px;
    line-height: 1.1;
    color: var(--ink);
    font-weight: 400;
  }
  .page-heading em { font-style: normal; font-weight: 700; color: var(--brand-blue); }
  .page-heading .line { display: block; }
  .body-copy {
    position: absolute;
    font-size: 5.5px;
    line-height: 8.3px;
    color: var(--body-ink);
    text-align: justify;
  }
  .body-copy p + p { margin-top: 10px; }

  .partner-photo {
    position: absolute;
    left: 0; top: 104px;
    width: 339px; height: 145px;
    background: linear-gradient(160deg, #dfe7e8 0%, #9fb58a 35%, #e9e0cf 65%, #d8c8ad 100%);
  }
  .partner-col-1 { left: 16px; top: 273px; width: 137px; }
  .partner-col-2 { left: 187px; top: 273px; width: 137px; }

  .philosophy-intro { left: 16px; top: 73px; width: 311px; }
  .philosophy-steps { left: 16px; top: 100px; width: 172px; }
  .philosophy-close { left: 16px; top: 229px; width: 311px; }
  .team-photo {
    position: absolute;
    left: 203px; top: 106px;
    width: 121px; height: 104px;
    background: linear-gradient(135deg, #7a5b46 0%, #4a3a30 50%, #24252b 100%);
  }

  .page-footer {
    position: absolute;
    left: 0; bottom: 0;
    width: 339px; height: 27px;
    background: var(--brand-blue);
    color: var(--paper);
    font-size: 4.2px;
    line-height: 6.5px;
    padding: 5px 10px 0 10px;
    display: flex; justify-content: space-between; align-items: center;
  }
  .page-footer .page-number { white-space: nowrap; padding-right: 6px; }
</style>
</head>
<body>

<section class="page page--cover">
  <div class="cover-photo" role="img" aria-label="Sunny mountain lake with a wooden pier and rocky shoreline"></div>
  <div class="cover-panel"></div>
  <div class="cover-logo-tab">
    <div class="cover-logo-name">KVO Wealth Management</div>
  </div>
  <h1 class="cover-title">
    <strong>Wealth Management Focused</strong>
    <span>On Your Needs &amp; Vision</span>
  </h1>
  <div class="cover-rule"></div>
</section>

<section class="page page--partner">
  <h2 class="page-heading"><em class="line">Partner</em><span class="line">with a Specialist</span></h2>
  <div class="partner-photo" role="img" aria-label="Multi-generation family walking along a boardwalk over sand dunes"></div>
  <div class="body-copy partner-col-1">
    <p>Understanding your unique needs and vision for the future is the starting point for our relationship. Together, we’ll assess where you are financially and where you want to be. Next, we’ll create a comprehensive wealth management plan that addresses your immediate and long-term goals. What about the unpredictable? We’ll plan for the changes that may be ahead, too.</p>
  </div>
  <div class="body-copy partner-col-2">
    <p>Exploring the topics of interest presented in this brochure will give you an idea of the depth and breadth of our services. Rest assured that we’ll partner with you throughout the planning process, always circling back to this fundamental question: what’s right for you and your loved ones?</p>
  </div>
  <footer class="page-footer">
    <span>Securities and advisory services offered through Meridian Harbor Financial Network, Member NRSA/ICPF, a Registered Investment Adviser<br>Fixed insurance products and services offered through Halvern Insurance Agency or The Baskin Collective</span>
    <span class="page-number">Page | 02</span>
  </footer>
</section>

<section class="page page--philosophy">
  <h2 class="page-heading"><em>Our</em> Philosophy</h2>
  <div class="body-copy philosophy-intro">
    <p>Our philosophy is based on empowering our clients through education. After taking the time to understand your goals, needs and challenges, we help you to understand and organize all aspects of your finances and create a plan of action.</p>
  </div>
  <div class="body-copy philosophy-steps">
    <p>The framework used to develop your plan is the 6-step Wealth Management Process, a flexible system that allows us to effectively customize a plan suited to your unique circumstances. During each step of the process, we take the time to provide a detailed explanation of our recommendations and why they are best suited for your situation.</p>
    <p>After all your questions have been answered, and you are confident in your decisions, we begin to implement a course of action. By actively learning and participating in the planning process, you retain control each step of the way. Once your investment program is implemented, we will monitor the performance of your investments and consult with you regularly to help ensure that the program continues to reflect your goals and objectives.</p>
  </div>
  <div class="team-photo" role="img" aria-label="Portrait of the three advisors in suits"></div>
  <div class="body-copy philosophy-close">
    <p>The Baskin Collective strives to develop a relationship in which you will feel more knowledgeable, informed and empowered as a result of working with us.</p>
  </div>
  <footer class="page-footer">
    <span>Securities and advisory services offered through Meridian Harbor Financial Network, Member NRSA/ICPF, a Registered Investment Adviser<br>Fixed insurance products and services offered through Halvern Insurance Agency or The Baskin Collective</span>
    <span class="page-number">Page | 03</span>
  </footer>
</section>

</body>
</html>
```